Flyer to hand out to masters graduate students - giving glimpse of our training and placement progra

We are an IT consulting company, specialized in IT Training and placement programs for the IT graduates(masters students).I have attached the sample files, which we used for our previous fliers. Text (matter) remains same, but we need a new design. New colors. New logo is attached. Please come up with good images.

This is half folded flyer, which contains 4 faces.

It Company

```html
<!DOCTYPE html>
<html lang="en">
<head>
<meta charset="utf-8">
<title>Meridian Data Works – Training &amp; Placement Flyer</title>
<link rel="stylesheet" href="https://fonts.googleapis.com/css2?family=Lato:wght@400;700&family=Roboto+Condensed:wght@300;400;700&display=swap">
<style>
  :root {
    --backdrop: #5b6a5f;
    --paper: #ffffff;
    --paper-shade: #e6e7e9;
    --ink: #3a3a3a;
    --ink-soft: #555;
    --muted: #8a8a8a;
    --brand-blue: #1d6fb8;
    --brand-blue-dark: #0f5596;
    --brand-orange: #f5921e;
    --charcoal: #3b3b3d;
    --charcoal-light: #5a5a5c;
    --sky: #bfdcf2;
    --sand: #d9c3a0;
  }
  * { box-sizing: border-box; margin: 0; padding: 0; }
  html, body { width: 1200px; height: 892px; overflow: hidden; }
  body { background: var(--backdrop); font-family: "Lato", sans-serif; color: var(--ink); }

  .spread {
    position: absolute; left: 40px; top: 40px;
    width: 1120px; height: 812px;
    display: flex; box-shadow: 0 10px 30px rgba(0,0,0,.35);
  }
  .panel { position: relative; width: 560px; height: 812px; overflow: hidden; }

  /* ---------- back panel ---------- */
  .panel--back { background: linear-gradient(160deg, var(--paper-shade) 0%, var(--paper) 45%, var(--paper-shade) 100%); }
  .intro { position: absolute; top: 56px; left: 50px; right: 50px; text-align: center; font-size: 15.5px; line-height: 1.4; color: var(--ink-soft); }
  .intro p + p { margin-top: 20px; }

  .art-circle { position: absolute; border-radius: 50%; border: 6px solid #c9c9cb; }
  .art-circle--opening { left: 40px; top: 262px; width: 240px; height: 240px; background: radial-gradient(circle at 50% 35%, #dcebf7, var(--sky)); }
  .art-circle--hiring { left: 310px; top: 250px; width: 210px; height: 210px; background: radial-gradient(circle at 50% 40%, #ead9bd, var(--sand)); }

  .contact-band { position: absolute; left: 0; bottom: 0; width: 560px; height: 460px; }
  .contact { position: absolute; left: 0; right: 0; bottom: 26px; text-align: center; color: #fff; }
  .contact__title { font-family: "Roboto Condensed", sans-serif; font-weight: 400; font-size: 34px; line-height: 1.1; letter-spacing: 1px; display: flex; justify-content: center; align-items: center; gap: 22px; margin-bottom: 12px; }
  .contact__title::before, .contact__title::after { content: ""; width: 4px; height: 30px; background: var(--brand-blue); }
  .contact__item { display: flex; flex-direction: column; align-items: center; font-size: 16px; line-height: 1.3; margin-top: 6px; }
  .contact__item svg { width: 16px; height: 16px; margin-bottom: 2px; }
  .contact__phone { font-weight: 700; font-size: 20px; }
  .contact__phone small { font-weight: 400; font-size: 16px; color: #ddd; margin-left: 8px; }

  /* ---------- front panel ---------- */
  .panel--front { background: var(--paper); }
  .brand { position: absolute; top: 58px; left: 0; right: 0; display: flex; justify-content: center; align-items: center; gap: 10px; }
  .brand__mark { width: 26px; height: 26px; border-radius: 50%; background: var(--brand-blue); }
  .brand__name { font-family: "Lato", sans-serif; font-weight: 700; font-size: 22px; letter-spacing: 1px; color: var(--brand-blue); }

  .hero { position: absolute; left: 0; top: 0; width: 560px; height: 520px; }
  .headline { position: absolute; top: 450px; right: 40px; font-family: "Roboto Condensed", sans-serif; white-space: nowrap; }
  .headline__lead { font-weight: 300; font-size: 36px; color: var(--muted); }
  .headline__key { font-weight: 700; font-size: 52px; color: var(--brand-blue); }

  .about { position: absolute; top: 530px; left: 40px; right: 40px; text-align: center; font-size: 11.5px; line-height: 1.45; color: var(--ink); }
  .about p + p { margin-top: 10px; }
  .web { position: absolute; top: 742px; left: 0; right: 0; text-align: center; font-size: 13px; letter-spacing: 3px; color: var(--brand-orange); }
</style>
</head>
<body>
<main class="spread">

  <section class="panel panel--back">
    <div class="intro">
      <p>For the fresh graduates (OPT/CPT), Meridian Data is a learning ground, an opportunity for growth, a stepping stone in the career graph and a substantial elevator for an excellent future.</p>
      <p>We are currently hiring students who completed their MBA/MS/BS graduates with or without IT background and who are on OPT/CPT status.</p>
    </div>

    <div class="art-circle art-circle--opening" role="img" aria-label="Illustration of an empty office chair holding a Job Opening sign"></div>
    <div class="art-circle art-circle--hiring" role="img" aria-label="Illustration of a blue hanging Now Hiring sign"></div>

    <svg class="contact-band" viewBox="0 0 560 460" aria-hidden="true">
      <path d="M0,218 Q300,140 560,0 L560,460 L0,460 Z" fill="var(--brand-orange)"/>
      <path d="M0,232 Q300,154 560,14 L560,460 L0,460 Z" fill="var(--charcoal)"/>
    </svg>

    <div class="contact">
      <h2 class="contact__title">CONTACT US</h2>
      <div class="contact__item">
        <svg viewBox="0 0 24 24"><path fill="var(--brand-blue)" d="M6.6 10.8a15 15 0 0 0 6.6 6.6l2.2-2.2c.3-.3.7-.4 1-.2 1.1.4 2.3.6 3.6.6.6 0 1 .4 1 1V20c0 .6-.4 1-1 1A17 17 0 0 1 3 4c0-.6.4-1 1-1h3.5c.6 0 1 .4 1 1 0 1.3.2 2.5.6 3.6.1.3 0 .7-.2 1z"/></svg>
        <span class="contact__phone">(555)014-2290<small>Ext : 312</small></span>
      </div>
      <div class="contact__item">
        <svg viewBox="0 0 24 24"><rect x="2" y="5" width="20" height="14" rx="1" fill="var(--brand-blue)"/><path d="M2 6l10 7 10-7" stroke="#fff" stroke-width="1.5" fill="none"/></svg>
        <span>info@meridiandataworks.com</span>
      </div>
      <div class="contact__item">
        <svg viewBox="0 0 24 24"><circle cx="12" cy="12" r="10" fill="var(--brand-blue)"/><path d="M2 12h20M12 2c3 3 3 17 0 20M12 2c-3 3-3 17 0 20" stroke="#fff" stroke-width="1.2" fill="none"/></svg>
        <span>www.meridiandataworks.com</span>
      </div>
      <div class="contact__item">
        <svg viewBox="0 0 24 24"><path fill="var(--brand-blue)" d="M12 2a7 7 0 0 0-7 7c0 5 7 13 7 13s7-8 7-13a7 7 0 0 0-7-7zm0 9.5A2.5 2.5 0 1 1 12 6.5a2.5 2.5 0 0 1 0 5z"/></svg>
        <span>48 Harbor Park Dr, Ste 210, Linden Falls, NJ 07099</span>
      </div>
    </div>
  </section>

  <section class="panel panel--front">
    <svg class="hero" viewBox="0 0 560 520" aria-hidden="true">
      <defs>
        <linearGradient id="photoTone" x1="0" y1="0" x2="1" y2="1">
          <stop offset="0" stop-color="#dfe9f1"/>
          <stop offset=".5" stop-color="#9fbcd6"/>
          <stop offset="1" stop-color="#eef2f5"/>
        </linearGradient>
      </defs>
      <path d="M0,212 Q250,200 560,120" stroke="var(--brand-blue)" stroke-width="3" fill="none"/>
      <path d="M0,222 Q250,210 560,130 L560,340 Q300,470 0,470 Z" fill="url(#photoTone)"/>
      <path d="M0,470 Q300,470 560,340 L560,356 Q300,490 0,486 Z" fill="var(--brand-orange)"/>
    </svg>
    <div class="hero" style="clip-path: polygon(0 43%, 100% 25%, 100% 65%, 0 90%);" role="img" aria-label="Photo of three young professionals smiling while working together at a laptop"></div>

    <div class="brand">
      <span class="brand__mark"></span>
      <span class="brand__name">MERIDIAN DATA WORKS</span>
    </div>

    <h1 class="headline"><span class="headline__lead">For all your </span><span class="headline__key">IT NEEDS</span></h1>

    <div class="about">
      <p>Meridian Data is one of the leading IT consulting companies in US, with over 17 years proven industry track record, having leading enterprise companies as our clients &amp; training on cutting edge technologies. We are pioneers in training &amp; placements from Linden Falls, New Jersey with global presence in US and India. We distinguish ourselves from others through a quality of education, engineered by a dexterous mix of established teaching ideologies, modern methodologies and technically qualified instructors. Meridian Data's methodologies make learning an enjoyable as well as a rewarding experience.</p>
      <p>Meridian Data is currently hiring fresh graduates (OPT/CPT), willing to join us as Full-Time employees or Interns to cater the IT needs of our clients across USA. We provide free, top notch training, excellent accommodation and 100% guaranteed placements with H1B and green card sponsorship.</p>
    </div>

    <p class="web">www.meridiandataworks.com</p>
  </section>

</main>
</body>
</html>
```